Darrow Consulting needs a quality & professional business card!

I am a recruitment and employment consultant from Brisbane, Australia and I had a fantastic logo organised by this community to I am hoping the business card will be the same.

I have attached the Darrow consulting logo that ideally would feature on the back of the business card. There are a number of logos for you to use as you see fit. I would like the colour cheme to match that of the Darrow Consulting logo. I also have a secondary company called Career Lantern Australia and I have included that logo as well. While it is an important part of the business I don't want this logo feature too predominantly as I am moving out of this space. This logo was created by myself and is of low quality. Feel free to use the icon and words however you want. The winning design will be smart, professional and eye-catching.

The information I am looking for in the business card is:
Name: Gavin Darrow
Position: Founder & Director
Phone: (07) 3519 6482
Mobile: 0431 586 207
Email: gavin@careerlantern.com.au

Target Market(s)

Recruiters, government, large companies

Contact Information for Business Card

Name: Gavin Darrow
Phone: (07) 3519 6482
Mobile: 0431 586 207
Web: www.careerlantern.com.au

Font styles to use
Serif
Sans Serif

Requirements
Must have
• Darrow Consulting Logo on reverse side
• Contact details on front side with smaller reference to Darrow Consulting logo and Career Lantern Australia logo

```html
<!DOCTYPE html>
<html lang="en">
<head>
<meta charset="utf-8">
<title>Darrow Consulting – Business Card</title>
<link rel="stylesheet" href="https://fonts.googleapis.com/css2?family=Montserrat:wght@300;400&family=Roboto:wght@300;400&display=swap">
<style>
  :root {
    --backdrop: #ec0f33;
    --card-black: #050505;
    --arc-grey: #212121;
    --dot-grey: #4a4a4a;
    --dot-grey-light: #595959;
    --logo-grey: #d4d4d4;
    --card-white: #ffffff;
    --sky: #9dd4e8;
    --apricot: #e9a96c;
    --apricot-deep: #d9975a;
    --leaf: #63c083;
    --mint: #4bc68a;
    --ink: #1d1d1d;
    --ink-soft: #3a4a52;
  }
  * { margin: 0; padding: 0; box-sizing: border-box; }
  html, body { width: 1200px; height: 1200px; overflow: hidden; }
  body {
    background: var(--backdrop);
    font-family: "Roboto", Arial, sans-serif;
    position: relative;
  }
  .card {
    position: absolute;
    left: 180px;
    width: 840px;
    height: 490px;
    border-radius: 14px;
    overflow: hidden;
    box-shadow: 0 18px 40px rgba(80, 0, 10, 0.35);
  }
  .card-back { top: 80px; background: var(--card-black); }
  .card-front { top: 630px; background: var(--card-white); }
  .card svg.decor { position: absolute; inset: 0; }

  .brand-lockup {
    position: absolute;
    left: 0; right: 0;
    top: 188px;
    text-align: center;
    font-family: "Montserrat", Arial, sans-serif;
    font-weight: 300;
    color: var(--logo-grey);
  }
  .brand-name { font-size: 58px; letter-spacing: 4px; line-height: 1; }
  .brand-sub { font-size: 22px; letter-spacing: 12px; margin-top: 6px; }

  .side-brand {
    position: absolute;
    left: 520px;
    top: 118px;
    display: flex;
    align-items: center;
    gap: 14px;
    color: var(--ink);
    font-weight: 400;
  }
  .side-brand-dot {
    width: 44px; height: 44px;
    border-radius: 50%;
    background: var(--ink);
  }
  .side-brand-name { font-size: 30px; line-height: 1; }
  .side-brand-region { font-size: 15px; margin-top: 4px; }

  .person {
    position: absolute;
    left: 72px;
    top: 232px;
    color: var(--ink);
  }
  .person-name { font-size: 40px; letter-spacing: 1px; line-height: 1; }
  .person-first { font-weight: 300; }
  .person-last { font-weight: 400; }
  .person-role { font-size: 15px; font-weight: 300; margin-top: 6px; margin-left: 10px; }

  .contacts {
    position: absolute;
    left: 120px;
    top: 340px;
    list-style: none;
    color: var(--ink-soft);
    font-size: 15px;
    font-weight: 300;
  }
  .contact {
    display: flex;
    align-items: center;
    gap: 10px;
    height: 30px;
  }
  .contact-icon {
    width: 22px; height: 22px;
    border-radius: 50%;
    background: var(--card-white);
    display: flex;
    align-items: center;
    justify-content: center;
  }
</style>
</head>
<body>

<section class="card card-back" aria-label="Card reverse">
  <svg class="decor" width="840" height="490" viewBox="0 0 840 490">
    <circle cx="724" cy="504" r="430" fill="var(--arc-grey)"/>
    <circle cx="130" cy="30" r="48" fill="var(--dot-grey-light)"/>
    <circle cx="438" cy="6" r="74" fill="var(--dot-grey)"/>
    <circle cx="53" cy="443" r="61" fill="var(--dot-grey)"/>
  </svg>
  <div class="brand-lockup">
    <div class="brand-name">DARROW</div>
    <div class="brand-sub">CONSULTING</div>
  </div>
</section>

<section class="card card-front" aria-label="Card front">
  <svg class="decor" width="840" height="490" viewBox="0 0 840 490">
    <circle cx="270" cy="610" r="440" fill="var(--sky)"/>
    <circle cx="330" cy="40" r="66" fill="var(--apricot)"/>
    <circle cx="0" cy="255" r="30" fill="var(--apricot-deep)"/>
    <circle cx="560" cy="24" r="48" fill="var(--leaf)"/>
    <circle cx="610" cy="300" r="48" fill="var(--leaf)"/>
    <circle cx="838" cy="330" r="44" fill="var(--mint)"/>
  </svg>

  <div class="side-brand">
    <span class="side-brand-dot"></span>
    <div>
      <div class="side-brand-name">Career Lantern</div>
      <div class="side-brand-region">Australia</div>
    </div>
  </div>

  <div class="person">
    <div class="person-name"><span class="person-first">GAVIN</span> <span class="person-last">DARROW</span></div>
    <div class="person-role">Founder &amp; Director</div>
  </div>

  <ul class="contacts">
    <li class="contact">
      <span class="contact-icon">
        <svg width="12" height="12" viewBox="0 0 12 12"><path d="M2.5 1.2l2 2-1 1.2a6 6 0 0 0 3.6 3.6l1.2-1 2 2-1.3 1.5C5 10.2 1.8 7 1 2.5z" fill="var(--sky)"/></svg>
      </span>0431 586 207
    </li>
    <li class="contact">
      <span class="contact-icon">
        <svg width="12" height="12" viewBox="0 0 12 12"><rect x="3.5" y="1" width="5" height="10" rx="1" fill="none" stroke="var(--sky)" stroke-width="1.2"/></svg>
      </span>(07) 3519 6482
    </li>
    <li class="contact">
      <span class="contact-icon">
        <svg width="12" height="12" viewBox="0 0 12 12"><circle cx="6" cy="6" r="4.6" fill="none" stroke="var(--sky)" stroke-width="1.1"/><path d="M1.4 6h9.2M6 1.4c-2.4 2.6-2.4 6.6 0 9.2M6 1.4c2.4 2.6 2.4 6.6 0 9.2" fill="none" stroke="var(--sky)" stroke-width="0.9"/></svg>
      </span>www.careerlantern.com.au
    </li>
    <li class="contact">
      <span class="contact-icon">
        <svg width="12" height="12" viewBox="0 0 12 12"><rect x="1.5" y="3" width="9" height="6.5" rx="0.8" fill="none" stroke="var(--sky)" stroke-width="1.1"/><path d="M1.8 3.4L6 6.6l4.2-3.2" fill="none" stroke="var(--sky)" stroke-width="1"/></svg>
      </span>gavin@careerlantern.com.au
    </li>
  </ul>
</section>

</body>
</html>
```